AUDITING SERVICES FOR IMPORT/EXPORT/LOGISTICS

* PROCUREMENT OF PARTS / SERVICES
* BOAT POSITIONING

Industry/Entity Type

Auditing

Contact Information for Business Card

KTF CONSULTANTS
(WILLOW HARBOUR CRAFT PTY LTD) 17 THE ESPLANADE CORELLA SHORES
DAVID FENWICK 0418274603 LOUISE-JANE FENWICK 0418274681 (ON OPPOSITE SIDE)

```html
<!DOCTYPE html>
<html lang="en">
<head>
<meta charset="utf-8">
<title>KTF Consultants – Business Card</title>
<link href="https://fonts.googleapis.com/css2?family=Michroma&family=Mulish:wght@400;500&display=swap" rel="stylesheet">
<style>
  :root {
    --bg-deep: #050607;
    --bg-mid: #14181c;
    --brand-blue: #2f4fb0;
    --service-blue: #4a5fc0;
    --silver: #d9dde2;
    --silver-dark: #6d7277;
    --white: #ffffff;
  }
  html, body {
    margin: 0;
    padding: 0;
    width: 1200px;
    height: 702px;
    overflow: hidden;
    background: var(--bg-deep);
  }
  .card {
    position: relative;
    width: 1200px;
    height: 702px;
    overflow: hidden;
    background: radial-gradient(ellipse at 50% 30%, var(--bg-mid) 0%, #0b0d10 55%, var(--bg-deep) 100%);
    font-family: "Mulish", Arial, sans-serif;
    color: var(--white);
  }
  .brand-mark {
    position: absolute;
    top: 62px;
    left: 0;
    width: 100%;
    text-align: center;
    font-family: "Michroma", sans-serif;
    font-size: 116px;
    line-height: 150px;
    letter-spacing: 6px;
    color: var(--brand-blue);
  }
  .company-name {
    position: absolute;
    top: 236px;
    left: 0;
    width: 100%;
    text-align: center;
    font-family: "Michroma", sans-serif;
    font-size: 27px;
    letter-spacing: 2px;
    color: var(--silver);
  }
  .services {
    position: absolute;
    top: 276px;
    left: 0;
    width: 100%;
    margin: 0;
    padding: 0;
    list-style: none;
    text-align: center;
    font-family: "Michroma", sans-serif;
    font-size: 15px;
    line-height: 23px;
    letter-spacing: 3px;
    font-variant: small-caps;
    color: var(--service-blue);
  }
  .divider {
    position: absolute;
    top: 361px;
    left: 0;
    width: 100%;
    height: 17px;
    background: linear-gradient(180deg, var(--silver) 0%, #9aa0a6 50%, var(--silver-dark) 100%);
  }
  .contact {
    position: absolute;
    top: 430px;
    width: 560px;
    text-align: center;
  }
  .contact--left { left: 27px; }
  .contact--right { left: 599px; }
  .contact__name {
    font-size: 33px;
    font-weight: 400;
    letter-spacing: 1px;
    color: var(--brand-blue);
    line-height: 44px;
  }
  .contact__phone {
    font-size: 46px;
    font-weight: 500;
    letter-spacing: 3px;
    line-height: 58px;
  }
  .contact__email {
    font-size: 28px;
    line-height: 38px;
  }
  .address {
    position: absolute;
    top: 607px;
    left: 0;
    width: 100%;
    text-align: center;
    font-size: 33px;
    letter-spacing: 1px;
  }
</style>
</head>
<body>
  <div class="card">
    <div class="brand-mark">KTF</div>
    <div class="company-name">WILLOW HARBOUR CRAFT PTY LTD</div>
    <ul class="services">
      <li>Import / Export Services</li>
      <li>Procurement of Parts &amp; Services</li>
      <li>Boat Positioning</li>
    </ul>
    <div class="divider"></div>
    <div class="contact contact--left">
      <div class="contact__name">DAVID FENWICK</div>
      <div class="contact__phone">0418 274 603</div>
      <div class="contact__email">david@willowharbourcraft.com</div>
    </div>
    <div class="contact contact--right">
      <div class="contact__name">LOUISE-JANE FENWICK</div>
      <div class="contact__phone">0418 274 681</div>
      <div class="contact__email">louisejane@willowharbourcraft.com</div>
    </div>
    <div class="address">17 The Esplanade Corella Shores Qld 4590</div>
  </div>
</body>
</html>
```